graphic showing our process of education as a process called a pipeline

Also see my updated comments on discussion section.
Title of the graphic needs to be:
TITLE = The KELIMO Strategic Leadership Pipeline = larger, bold heading
SUB-TITLE = Developing a steady flow of servant leaders for Tanzania's future = under title; smaller font
change the text for each of the 7 steps to match the outcomes listed on the newly attached PDF (strategic pipeline 11x17)
Pipe should be straight or mostly straight.
Pipe should not be in a strong or dark color.
Any icons or symbols should be simple and professional, not like cartoon or childish.
We need a graphic design that shows our PROCESS, called a "pipeline," that is creating future leaders. We are a US-based non-profit that operates a Christian school in rural Tanzania for 600 students (pre-K through 12th grade). It starts with child sponsorship program that allows poor children and orphans to attend school, we have a primary school (like USA elementary school, pre-K thru 7th), and are building a secondary boarding school (like USA middle and high school, grades 8-12), where students will live on campus in dormitories. We offer education, scholarships, leadership development experiences, help finding and securing college scholarships, academic and career counseling, placements for internships and jobs, and networking and leadership development content and events to create the next generation of servant leaders for the country. Prominent colors should probably be the green, blue and black in the Tanzania flag; we want the design to communicate "smart" and "strategic." The stages of the pipeline need to be properly named; we need to show a "leak" in the pipeline after the primary school because we currently have to send our students AWAY to other boarding schools because we don't have one. As the attached recording says, this is bad for their progress. The attached pipeline graphic is very rough and NOT meant to be imitated. It is factually correct, but is busy and not attractive.

Target Market(s)

Major financial contributors and foundations that want to give money to the cause

Industry/Entity Type

non-profit/Christian ministry in education

Font styles to use
Sans Serif

Requirements
Must have
• A "smart" and strategic" feel; preferably visible when on a half page
Nice to have
• a smart, sophisticated, serious look and feel
Should not have
• an elementary school feel

```html
<!DOCTYPE html>
<html lang="en">
<head>
<meta charset="utf-8">
<title>KELIMO Leadership Pipeline</title>
<link rel="stylesheet" href="https://fonts.googleapis.com/css2?family=Montserrat:wght@500;600;700&family=Open+Sans:wght@400;600&display=swap">
<style>
  :root {
    --brand-blue: #1b9ad6;
    --brand-green: #2eb34b;
    --ink: #1a1a1a;
    --pipe-grey: #dcdcdc;
    --paper: #ffffff;
    --leak-blue: #3fa9e6;
  }
  * { box-sizing: border-box; margin: 0; padding: 0; }
  html, body { width: 1200px; height: 1200px; overflow: hidden; background: var(--paper); }
  .canvas { position: relative; width: 1200px; height: 1200px; overflow: hidden; background: var(--paper); }

  .pipeline-panel { position: absolute; left: 0; width: 1200px; height: 581px; }
  .pipeline-panel--with-leak { top: 0; }
  .pipeline-panel--sealed { top: 581px; }

  .panel-title {
    position: absolute; top: 124px; left: 0; width: 1200px; text-align: center;
    font-family: "Montserrat", sans-serif; font-weight: 700; font-size: 42px; line-height: 1;
    color: var(--brand-blue); letter-spacing: 0.2px;
  }
  .panel-subtitle {
    position: absolute; top: 179px; left: 0; width: 1200px; text-align: center;
    font-family: "Montserrat", sans-serif; font-weight: 500; font-size: 20px; line-height: 1;
    color: var(--ink);
  }
  .subtitle-rule { position: absolute; top: 190px; height: 2px; background: var(--brand-green); width: 64px; }
  .subtitle-rule--left { left: 208px; }
  .subtitle-rule--right { left: 934px; }

  .stage { position: absolute; top: 230px; width: 104px; margin-left: -52px; }
  .stage-label {
    height: 53px; background: var(--brand-blue); color: var(--paper);
    display: flex; align-items: center; justify-content: center; text-align: center;
    font-family: "Montserrat", sans-serif; font-weight: 700; font-size: 8px; line-height: 1.2;
    text-transform: uppercase; padding: 0 6px;
  }
  .stage-icon {
    width: 40px; height: 44px; margin: 10px auto 0; border-radius: 6px; background: var(--brand-green);
  }
  .stage-connector {
    width: 0; height: 60px; margin: 15px auto 0; border-left: 2px dotted var(--brand-blue);
  }
  .stage-outcome {
    position: absolute; top: 236px; left: 2px; width: 100px; text-align: center; white-space: nowrap;
    font-family: "Open Sans", sans-serif; font-size: 8.5px; line-height: 1.2; color: var(--ink);
  }

  .stage--sponsorship { left: 217px; }
  .stage--primary { left: 349px; }
  .stage--secondary { left: 476px; }
  .stage--service { left: 609px; }
  .stage--higher-ed { left: 733px; }
  .stage--employment { left: 862px; }
  .stage--hub { left: 987px; }

  .stage--sponsorship .stage-outcome { left: 3px; }
  .stage--primary .stage-outcome { left: 1px; }
  .stage--secondary .stage-outcome { left: 17px; }
  .stage--service .stage-outcome { left: 3px; }
  .stage--higher-ed .stage-outcome { left: 17px; }
  .stage--employment .stage-outcome { left: 13px; }
  .stage--hub .stage-outcome { left: 16px; }

  .pipe { position: absolute; top: 420px; left: 262px; width: 808px; height: 28px; background: var(--pipe-grey); }
  .pipe-cap { position: absolute; top: 416px; width: 9px; height: 36px;
    border-left: 3px solid var(--brand-blue); border-right: 3px solid var(--brand-blue); }
  .pipe-cap--start { left: 258px; }
  .pipe-cap--end { left: 1065px; }

  .intake-arrow { position: absolute; top: 412px; left: 214px; width: 50px; height: 28px; }

  .leak-marker { position: absolute; top: 424px; left: 408px; width: 28px; height: 60px; }
</style>
</head>
<body>
<main class="canvas">

  <section class="pipeline-panel pipeline-panel--with-leak" aria-label="Pipeline with leak after primary school">
    <h1 class="panel-title">KELIMO Leadership Pipeline</h1>
    <span class="subtitle-rule subtitle-rule--left"></span>
    <p class="panel-subtitle">Developing a steady flow of servant leaders for Tanzania's</p>
    <span class="subtitle-rule subtitle-rule--right"></span>

    <div class="pipe"></div>
    <span class="pipe-cap pipe-cap--start"></span>
    <span class="pipe-cap pipe-cap--end"></span>
    <svg class="intake-arrow" viewBox="0 0 50 28" aria-hidden="true">
      <path d="M3 2 Q8 18 40 20" fill="none" stroke="#1b9ad6" stroke-width="2" stroke-dasharray="2 3"/>
      <path d="M38 15 L46 20 L38 25 Z" fill="#1b9ad6"/>
    </svg>
    <svg class="leak-marker" viewBox="0 0 28 60" role="img" aria-label="Leak: crack in the pipe with water drops falling after primary school">
      <path d="M14 2 L10 12 L15 12 L11 22 L19 10 L14 10 L17 2 Z" fill="#3fa9e6"/>
      <path d="M9 30 C5 37 3 41 3 44 A6 6 0 0 0 15 44 C15 41 13 37 9 30 Z" fill="#3fa9e6"/>
      <path d="M19 38 C15 45 13 49 13 52 A6 6 0 0 0 25 52 C25 49 23 45 19 38 Z" fill="#1b9ad6"/>
    </svg>

    <div class="stage stage--sponsorship">
      <div class="stage-label">Sponsorship<br>Program</div>
      <div class="stage-icon" role="img" aria-label="Icon of an adult with a child"></div>
      <div class="stage-connector"></div>
      <p class="stage-outcome">Children renewed<br>by spiritual<br>, academic, and<br>health foundations</p>
    </div>
    <div class="stage stage--primary">
      <div class="stage-label">Primary<br>School</div>
      <div class="stage-icon" role="img" aria-label="Icon of a child"></div>
      <div class="stage-connector"></div>
      <p class="stage-outcome">Potential leaders<br>with Biblical<br>worldview and<br>strong academic<br>foundations.</p>
    </div>
    <div class="stage stage--secondary">
      <div class="stage-label">Secondary<br>School</div>
      <div class="stage-icon" role="img" aria-label="Icon of a student with a science symbol"></div>
      <div class="stage-connector"></div>
      <p class="stage-outcome">Emerging leaders<br>with concrete<br>skills and<br>strong servant<br>mindset.</p>
    </div>
    <div class="stage stage--service">
      <div class="stage-label">Service<br>Leadership<br>Experience</div>
      <div class="stage-icon" role="img" aria-label="Icon of a person helping another up"></div>
      <div class="stage-connector"></div>
      <p class="stage-outcome">Growing servant<br>leaders with<br>practical<br>experience<br>to effect change<br>for the kingdom</p>
    </div>
    <div class="stage stage--higher-ed">
      <div class="stage-label">Higher<br>Education<br>Support</div>
      <div class="stage-icon" role="img" aria-label="Icon of a graduate"></div>
      <div class="stage-connector"></div>
      <p class="stage-outcome">Visionary leaders<br>with expanded<br>capability to solve<br>Tanzania's<br>biggest challenges</p>
    </div>
    <div class="stage stage--employment">
      <div class="stage-label">Employment<br>Center</div>
      <div class="stage-icon" role="img" aria-label="Icon of a person walking with a briefcase"></div>
      <div class="stage-connector"></div>
      <p class="stage-outcome">Capable Christ-<br>centered leaders<br>in the marketplace<br>as value adding<br>employees and<br>entrepreneurs.</p>
    </div>
    <div class="stage stage--hub">
      <div class="stage-label">Leadership<br>Hub</div>
      <div class="stage-icon" role="img" aria-label="Icon of a crowd of people" style="width:50px"></div>
      <div class="stage-connector"></div>
      <p class="stage-outcome">Mature Christian<br>leaders being<br>placed and<br>positioned for<br>leadership roles<br>in the community<br>and nation.</p>
    </div>
  </section>

  <section class="pipeline-panel pipeline-panel--sealed" aria-label="Pipeline without leak">
    <h2 class="panel-title">KELIMO Leadership Pipeline</h2>
    <span class="subtitle-rule subtitle-rule--left"></span>
    <p class="panel-subtitle">Developing a steady flow of servant leaders for Tanzania's</p>
    <span class="subtitle-rule subtitle-rule--right"></span>

    <div class="pipe"></div>
    <span class="pipe-cap pipe-cap--start"></span>
    <span class="pipe-cap pipe-cap--end"></span>
    <svg class="intake-arrow" viewBox="0 0 50 28" aria-hidden="true">
      <path d="M3 2 Q8 18 40 20" fill="none" stroke="#1b9ad6" stroke-width="2" stroke-dasharray="2 3"/>
      <path d="M38 15 L46 20 L38 25 Z" fill="#1b9ad6"/>
    </svg>

    <div class="stage stage--sponsorship">
      <div class="stage-label">Sponsorship<br>Program</div>
      <div class="stage-icon" role="img" aria-label="Icon of an adult with a child"></div>
      <div class="stage-connector"></div>
      <p class="stage-outcome">Children renewed<br>by spiritual<br>, academic, and<br>health foundations</p>
    </div>
    <div class="stage stage--primary">
      <div class="stage-label">Primary<br>School</div>
      <div class="stage-icon" role="img" aria-label="Icon of a child"></div>
      <div class="stage-connector"></div>
      <p class="stage-outcome">Potential leaders<br>with Biblical<br>worldview and<br>strong academic<br>foundations.</p>
    </div>
    <div class="stage stage--secondary">
      <div class="stage-label">Secondary<br>School</div>
      <div class="stage-icon" role="img" aria-label="Icon of a student with a science symbol"></div>
      <div class="stage-connector"></div>
      <p class="stage-outcome">Emerging leaders<br>with concrete<br>skills and<br>strong servant<br>mindset.</p>
    </div>
    <div class="stage stage--service">
      <div class="stage-label">Service<br>Leadership<br>Experience</div>
      <div class="stage-icon" role="img" aria-label="Icon of a person helping another up"></div>
      <div class="stage-connector"></div>
      <p class="stage-outcome">Growing servant<br>leaders with<br>practical<br>experience<br>to effect change<br>for the kingdom</p>
    </div>
    <div class="stage stage--higher-ed">
      <div class="stage-label">Higher<br>Education<br>Support</div>
      <div class="stage-icon" role="img" aria-label="Icon of a graduate"></div>
      <div class="stage-connector"></div>
      <p class="stage-outcome">Visionary leaders<br>with expanded<br>capability to solve<br>Tanzania's<br>biggest challenges</p>
    </div>
    <div class="stage stage--employment">
      <div class="stage-label">Employment<br>Center</div>
      <div class="stage-icon" role="img" aria-label="Icon of a person walking with a briefcase"></div>
      <div class="stage-connector"></div>
      <p class="stage-outcome">Capable Christ-<br>centered leaders<br>in the marketplace<br>as value adding<br>employees and<br>entrepreneurs.</p>
    </div>
    <div class="stage stage--hub">
      <div class="stage-label">Leadership<br>Hub</div>
      <div class="stage-icon" role="img" aria-label="Icon of a crowd of people" style="width:50px"></div>
      <div class="stage-connector"></div>
      <p class="stage-outcome">Mature Christian<br>leaders being<br>placed and<br>positioned for<br>leadership roles<br>in the community<br>and nation.</p>
    </div>
  </section>

</main>
</body>
</html>
```